Electrical Wholesaler Needs a New Website

Looking for a new website to be built for an electrical wholesaler based in Birmingham(England). Our logo is based on two Lions with a shield, so ideally the site should be deigned around that.

Looking for something that shows off our logo and incorporates what we are trying to do, preferably to have a colour scheme that is green and black if possible.

Reason: Still undecided on what I'm looking for

Reason: Need more time to decide

Target Market(s)

I'm looking for a professional website for my company that doesn't just look like amother WordPress template that I could build myself.

Industry/Entity Type

Electrical

Font styles to use
Sans Serif

Colors
9bcb3c
cadf82

Requirements
Must have
• Website with 4-5 pages, home page, about us, suppliers list, catalogue download and contact us. Search for UK electrical wholesalers to give you an idea of what I mean.

```html
<!DOCTYPE html>
<html lang="en">
<head>
<meta charset="utf-8">
<title>Crest Electrical Wholesalers – Home</title>
<link rel="stylesheet" href="https://fonts.googleapis.com/css2?family=Cabin:wght@400;600;700&family=Roboto+Condensed:wght@300;400&display=swap">
<style>
:root{
  --green:#9bcb3c;
  --green-pale:#cadf82;
  --green-bright:#8cc63f;
  --green-deep:#17452f;
  --ink:#1d3b2a;
  --text:#2b2b2b;
  --white:#ffffff;
  --line:#c9e08a;
}
*{box-sizing:border-box;margin:0;padding:0}
html,body{width:1200px;height:863px;overflow:hidden;background:var(--white)}
body{position:relative;font-family:"Cabin",sans-serif;color:var(--text)}
a{color:inherit;text-decoration:none}
.abs{position:absolute}

/* utility bar */
.utility{left:0;top:0;width:1200px;height:24px;font-size:11px;color:var(--ink)}
.utility-links{left:200px;top:4px;display:flex;gap:8px}
.utility-welcome{right:200px;top:4px}

/* header */
.masthead{left:0;top:24px;width:1200px;height:112px;background:var(--green-pale);border-bottom:4px solid var(--green)}
.brand{left:198px;top:38px;width:86px;display:flex;flex-direction:column;align-items:flex-start;gap:4px;color:var(--green-deep)}
.brand-mark{width:22px;height:22px;border-radius:50%;background:var(--green-deep)}
.brand-name{font-size:26px;font-weight:700;line-height:1}
.brand-sub{font-size:7px;font-weight:700;letter-spacing:.1px}
.main-nav{left:348px;top:96px;font-size:12px;font-weight:700;color:var(--ink)}
.main-nav a{position:absolute;white-space:nowrap}
.main-nav .current{color:var(--green-bright)}
.phone{left:894px;top:48px;width:108px;height:22px;background:var(--green);border-radius:2px;color:var(--white);font-size:11px;font-weight:700;display:flex;align-items:center;justify-content:flex-end;padding-right:4px;white-space:nowrap}
.search{left:858px;top:90px;width:144px;height:20px;background:var(--green);color:var(--white);font-size:11px;display:flex;align-items:center;padding-left:30px}
.badge-icon{position:absolute;left:0;top:-2px;width:22px;height:24px}

/* hero */
.headline{left:0;top:166px;width:1200px;text-align:center;font-size:50px;font-weight:700;color:var(--green-deep);letter-spacing:-.5px;white-space:nowrap}
.tagline{left:0;top:222px;width:1200px;text-align:center;font-family:"Roboto Condensed",sans-serif;font-weight:300;font-size:20px;color:var(--green-bright);letter-spacing:-.3px;white-space:nowrap}
.tagline sup{font-size:8px;color:var(--ink);margin-left:4px}
.decor{background:radial-gradient(ellipse at center,rgba(210,225,190,.35),rgba(255,255,255,0) 70%)}
.shield{width:166px;height:164px}
.shield-photo{position:absolute;background:linear-gradient(#f4f4f4,#cfd3d6);border-radius:4px}
.order{left:524px;top:469px;width:164px;height:32px;background:linear-gradient(#9fd14a,#6fb52c);border-radius:3px;color:var(--white);font-size:22px;font-family:"Roboto Condensed",sans-serif;font-weight:300;display:flex;align-items:center;justify-content:center;white-space:nowrap}
.chev{width:20px;height:36px}

/* top sellers */
.section-title{left:201px;top:557px;font-family:"Roboto Condensed",sans-serif;font-weight:300;font-size:24px;color:var(--green-bright);letter-spacing:-1px;white-space:nowrap}
.section-rule{left:198px;top:588px;width:803px;height:2px;background:var(--line)}
.section-rule::before{content:"";position:absolute;left:0;top:0;width:120px;height:2px;background:var(--green)}
.sellers{left:198px;top:592px;width:803px;height:131px;border:1px solid #e6efd0;border-bottom:3px solid var(--green-pale);box-shadow:0 2px 2px rgba(0,0,0,.08)}
.product{width:116px;height:114px;border:1px solid #dfe8cc;background:var(--white);text-align:center;font-family:"Roboto Condensed",sans-serif;font-weight:300;font-size:11px;line-height:16px;color:var(--green-bright);padding-top:78px;white-space:nowrap;overflow:hidden}
.product-photo{position:absolute;left:30px;top:14px;width:56px;height:56px;background:linear-gradient(#eceeef,#b9bec2);border-radius:6px}

/* suppliers */
.suppliers{left:198px;top:757px;width:803px;height:32px}
.supplier{position:absolute;top:0;height:32px;display:flex;align-items:center;justify-content:center;font-size:17px;font-weight:700;white-space:nowrap}

/* footer */
.footer{left:0;top:823px;width:1200px;height:40px;background:var(--green-deep);color:var(--white);font-size:11.5px;display:flex;align-items:center;justify-content:center}
</style>
</head>
<body>

<div class="abs utility">
  <nav class="abs utility-links"><a href="#">Home</a><a href="#">News</a><a href="#">My Account</a><a href="#">Shopping Cart</a></nav>
  <div class="abs utility-welcome">Welcome visitor you can <a href="#">login</a> or <a href="#">create an account</a></div>
</div>

<header class="abs masthead"></header>
<a class="abs brand" href="#">
  <span class="brand-mark"></span>
  <span class="brand-name">Crest</span>
  <span class="brand-sub">ELECTRICAL WHOLESALERS</span>
</a>
<nav class="abs main-nav">
  <a class="current" href="#" style="left:0">HOME</a>
  <a href="#" style="left:58px">ABOUT US</a>
  <a href="#" style="left:137px">SUPPLIERS LIST</a>
  <a href="#" style="left:240px">CATALOGUE DOWNLOAD</a>
  <a href="#" style="left:392px">CONTACT US</a>
</nav>
<div class="abs phone">
  <svg class="badge-icon" viewBox="0 0 22 24"><path d="M2 1h18v12c0 5-4 8-9 10C6 21 2 18 2 13z" fill="#fff" stroke="#1d3b2a" stroke-width="1.5"/><path d="M8 6c-1 3 1 8 5 10l1.5-1.5-2-2-1 .6c-1-1-2-3-2-4.5l1-.5-.7-2.6z" fill="#1d3b2a"/></svg>
  0800-555-0142
</div>
<div class="abs search">
  <svg class="badge-icon" viewBox="0 0 22 24"><path d="M2 1h18v12c0 5-4 8-9 10C6 21 2 18 2 13z" fill="#fff" stroke="#1d3b2a" stroke-width="1.5"/><circle cx="12" cy="9" r="4" fill="none" stroke="#1d3b2a" stroke-width="1.5"/><path d="M9 12l-4 4" stroke="#1d3b2a" stroke-width="2"/></svg>
  SEARCH HERE
</div>

<h1 class="abs headline">Over 30,000 Products in Stock</h1>
<p class="abs tagline">Free Next Day Delivery On Order Over £50<sup>+VAT</sup></p>

<div class="abs decor" role="img" aria-label="Faint heraldic decoration on the left" style="left:198px;top:254px;width:150px;height:260px"></div>
<div class="abs decor" role="img" aria-label="Faint heraldic decoration on the right" style="left:850px;top:254px;width:160px;height:260px"></div>

<svg width="0" height="0" style="position:absolute">
  <defs>
    <linearGradient id="shieldFill" x1="0" y1="0" x2="0" y2="1">
      <stop offset="0" stop-color="#a6d631"/><stop offset="1" stop-color="#c6ea2c"/>
    </linearGradient>
  </defs>
</svg>

<div class="abs" style="left:339px;top:311px">
  <svg class="shield" viewBox="0 0 166 164"><path d="M2 2H164V82C164 120 124 146 83 162C42 146 2 120 2 82Z" fill="url(#shieldFill)" stroke="#1d4a2e" stroke-width="2.5"/></svg>
  <div class="shield-photo" role="img" aria-label="Remote-controlled socket set with handset" style="left:20px;top:26px;width:122px;height:80px"></div>
</div>
<div class="abs" style="left:515px;top:260px">
  <svg class="shield" viewBox="0 0 166 164"><path d="M2 2H164V82C164 120 124 146 83 162C42 146 2 120 2 82Z" fill="url(#shieldFill)" stroke="#1d4a2e" stroke-width="2.5"/></svg>
  <div class="shield-photo" role="img" aria-label="LED downlight fitting" style="left:36px;top:20px;width:104px;height:86px;border-radius:40px"></div>
</div>
<div class="abs" style="left:693px;top:311px">
  <svg class="shield" viewBox="0 0 166 164"><path d="M2 2H164V82C164 120 124 146 83 162C42 146 2 120 2 82Z" fill="url(#shieldFill)" stroke="#1d4a2e" stroke-width="2.5"/></svg>
  <div class="shield-photo" role="img" aria-label="Three-gang light switch" style="left:43px;top:27px;width:80px;height:78px"></div>
</div>

<svg class="abs chev" style="left:485px;top:469px" viewBox="0 0 20 36"><path d="M18 1L2 18l16 17" fill="none" stroke="#9bcb3c" stroke-width="1.5"/></svg>
<a class="abs order" href="#">ORDER NOW!</a>
<svg class="abs chev" style="left:707px;top:469px" viewBox="0 0 20 36"><path d="M2 1l16 17L2 35" fill="none" stroke="#9bcb3c" stroke-width="1.5"/></svg>

<h2 class="abs section-title">TOP SELLERS</h2>
<div class="abs section-rule"></div>
<section class="abs sellers">
  <svg class="abs chev" style="left:4px;top:46px" viewBox="0 0 20 36"><path d="M18 1L2 18l16 17" fill="none" stroke="#9bcb3c" stroke-width="1.5"/></svg>
  <div class="abs product" style="left:26px;top:8px"><div class="product-photo" role="img" aria-label="GU10 LED lamp"></div>6W LED GU10 COOL<br>WHITE 4000K RETRO FIT</div>
  <div class="abs product" style="left:152px;top:8px"><div class="product-photo" role="img" aria-label="Fire-rated downlight"></div>6W LED GU10 COOL<br>WHITE 4000K RETRO FIT</div>
  <div class="abs product" style="left:280px;top:8px"><div class="product-photo" role="img" aria-label="Chrome light switch"></div>6W LED GU10 COOL<br>WHITE 4000K RETRO FIT</div>
  <div class="abs product" style="left:406px;top:8px"><div class="product-photo" role="img" aria-label="Chrome ceiling light fitting"></div>6W LED GU10 COOL<br>WHITE 4000K RETRO FIT</div>
  <div class="abs product" style="left:533px;top:8px"><div class="product-photo" role="img" aria-label="Fire-rated downlight"></div>6W LED GU10 COOL<br>WHITE 4000K RETRO FIT</div>
  <div class="abs product" style="left:659px;top:8px"><div class="product-photo" role="img" aria-label="Chrome light switch"></div>6W LED GU10 COOL<br>WHITE 4000K RETRO FIT</div>
  <svg class="abs chev" style="left:778px;top:46px" viewBox="0 0 20 36"><path d="M2 1l16 17L2 35" fill="none" stroke="#9bcb3c" stroke-width="1.5"/></svg>
</section>

<div class="abs suppliers">
  <span class="supplier" style="left:0;width:120px;color:#1e4d9b">Arlenby</span>
  <span class="supplier" style="left:128px;width:120px;color:#1a1a1a">Hartwell</span>
  <span class="supplier" style="left:258px;width:150px;color:#1d9a46">Stellan Electric</span>
  <span class="supplier" style="left:412px;width:120px;color:#1a1a1a">Marlowe</span>
  <span class="supplier" style="left:540px;width:120px;color:#0a5aa5">Voltmark</span>
  <span class="supplier" style="left:668px;width:135px;color:#d3282e">Rowanbridge</span>
</div>

<footer class="abs footer">© Copyright Crestelectrical 2013. All Rights Reserved.</footer>

</body>
</html>
```